Bottle Labels for Beer (Cherry Beer)

The goal is to design an interesting labeling for a 0,33l bottle for a German beer. The bottle has three labels in total: front, back and "neckholder". The product that is relevant in the first shot is a cherry beer. Only this one is asked to design right now. The further labels will be designed later on as carry-on projects on ArtHive with the chosen design as framework.

Nevertheless the label now will affect the other labels later on for the beers. The label should contain a part that connects all beers to each other. This may be e.g. a part of the canvas that is stable across all front side labels, a character that repeats across all labels or something that connects in any other way the labels later on together. There should not just be simple systematic of a label that changes the colour to distinguish between the different kinds of beer later as the CI color palette limits this. Some beers have one label and then do it in red, green, brown, blue etc. to distinguish between the kinds. It is ok to reference to the beer's colour and a blue, white, black or, wood or paper colour change may be helpful to distinguish. The range of beers that will be introduced are at least for cherry (right now), honey beer, pale ale, IPA, amber, dark, pilsener.

FRONT LABEL
The label should contain the full logo or just the "B". If inconvenient, the label can come also without the logo or "B" when reflected strongly in the upper "neckholder label".

NECKHOLDER LABEL
The neckholder label is a front-side label at the bottleneck. I'm fine if this shows just the logo and nothing else. If you got great other ideas, just go for it.

BACKSIDE LABEL
The appearance on the backside label should enable a co-branding as some beers are done in co-operation with others (in this particular case with the cherry producers and their PVL logo with the cherries). If you split the label in half or put the two logos ("B" and PVL") together as they are both round, is up to you. A positioning in front of the company name might also be an option.
The general Idea is that the backside label is constant across all products (except text and specifications) and just the part for the supporter/partner changes. The backside label has to include the standard objects like EAN barcode, ingredients, net filling content etc.

THE BRAND
The CI colours or themes should be followed where possible. Colours out of CI may be used e.g. the red to relate to the cherry or display of a cherry. Other exeption is the part on the backside where the logo of the partner is shown. Some preferences: round better than cubism, handcraft better than high tech, nature better than industry.

The max. size of the labels is fixed due to technical reasons. Nevertheless, parts of the label may be printed dark brown as the bottle's colour to offer e.g. the appearance of a round label.

The files that describe some hints as well as the text are

I hope, you git interested inn this project and the upcoming designs for the other beers afterwards. For questions, just let me know. Thanks in advance!

Matthias

Target Market(s)

only local / regional customers for the cherry beer and tourists that visit one of the biggest cherry growing regions in Europe.

Requirements
Must have
• A reference to Falkmanns on at least one of the frontside labels. This can be the full logo with text falcons and the "B" of just the "B" if a discrete reference might be a better fit.
Nice to have
• declaration table that provides deeper insight in the specifics of the product for "insiders" like bitter units, alcohol, hops used etc.
Should not have
• too many colours. For the pallet dark blue to white and black to white feel free; green is to avoide, red may be used in this specific case as an exception to underline that it is a cherry beer.

```html
<!DOCTYPE html>
<html lang="de">
<head>
<meta charset="utf-8">
<title>Lindenauer Kirschrot – Front Label</title>
<link rel="stylesheet" href="https://fonts.googleapis.com/css2?family=Cinzel:wght@700&family=EB+Garamond:wght@400;500&display=swap">
<style>
  :root {
    --navy: #272750;
    --navy-deep: #1c1c3c;
    --silver-light: #f4f4f4;
    --white: #ffffff;
    --mark-grey: #6a6a72;
  }
  * { margin: 0; padding: 0; box-sizing: border-box; }
  html, body { width: 1200px; height: 1200px; overflow: hidden; background: var(--white); }
  .label {
    position: relative;
    width: 1200px;
    height: 1200px;
    overflow: hidden;
    background: radial-gradient(ellipse 75% 60% at 50% 35%, var(--white) 0%, var(--silver-light) 45%, #c9c9c9 100%);
    font-family: "EB Garamond", Georgia, serif;
  }
  .band { position: absolute; left: 0; width: 100%; }
  .band--top {
    top: 0;
    height: 70px;
    background: linear-gradient(to right, #4d4d4d, #cfcfcf 20%, #ffffff 50%, #cfcfcf 80%, #4d4d4d);
  }
  .band--top::after {
    content: "";
    position: absolute;
    left: 0; bottom: 0;
    width: 100%; height: 20px;
    background: linear-gradient(to right, #2e2e2e, #8a8a8a 20%, #b8b8b8 50%, #8a8a8a 80%, #2e2e2e);
    box-shadow: 0 4px 8px rgba(0,0,0,.35);
  }
  .band--bottom {
    bottom: 0;
    height: 72px;
    background: linear-gradient(to right, #4d4d4d, #cfcfcf 20%, #ffffff 50%, #cfcfcf 80%, #4d4d4d);
  }
  .band--bottom::before {
    content: "";
    position: absolute;
    left: 0; top: 0;
    width: 100%; height: 18px;
    background: linear-gradient(to right, #2e2e2e, #8a8a8a 20%, #b8b8b8 50%, #8a8a8a 80%, #2e2e2e);
    box-shadow: 0 -4px 8px rgba(0,0,0,.3);
  }
  .town-view {
    position: absolute;
    left: 0;
    top: 555px;
    width: 100%;
    height: 573px;
    background: linear-gradient(to bottom, rgba(230,230,236,0) 0%, rgba(150,150,170,.55) 12%, #5c5c78 32%, #9a9aae 48%, #4a4a66 66%, #2f2f4c 82%, #23233d 100%);
  }
  .region-mark {
    position: absolute;
    top: 118px;
    right: 36px;
    font-family: "EB Garamond", Georgia, serif;
    font-weight: 500;
    font-size: 44px;
    line-height: 1;
    color: var(--mark-grey);
    display: flex;
    align-items: center;
    gap: 14px;
  }
  .region-mark__square {
    width: 20px; height: 20px;
    background: var(--mark-grey);
  }
  .seal {
    position: absolute;
    left: 359px;
    top: 102px;
    width: 480px;
    height: 480px;
  }
  .seal__title {
    font-family: "Cinzel", "Times New Roman", serif;
    font-weight: 700;
    fill: var(--white);
    letter-spacing: 1px;
  }
  .seal__maker {
    font-family: "EB Garamond", Georgia, serif;
    font-weight: 500;
    fill: var(--white);
  }
  .spec {
    position: absolute;
    bottom: 92px;
    font-size: 27px;
    color: var(--white);
    text-shadow: 0 0 3px rgba(0,0,0,.5);
  }
  .spec--temp { left: 21px; }
  .spec--alc { right: 27px; }
</style>
</head>
<body>
<main class="label">
  <div class="band band--top"></div>

  <div class="town-view" role="img" aria-label="Historic copperplate engraving of a small river town with church towers, hills and riverbank trees"></div>

  <div class="region-mark"><span class="region-mark__square"></span>Lindenau Land</div>

  <svg class="seal" viewBox="0 0 480 480" aria-label="Lindenauer Kirschrot seal">
    <defs>
      <radialGradient id="sealSilver" cx="50%" cy="40%" r="60%">
        <stop offset="0%" stop-color="#ffffff"/>
        <stop offset="70%" stop-color="#cfcfcf"/>
        <stop offset="100%" stop-color="#6e6e6e"/>
      </radialGradient>
      <radialGradient id="sealNavy" cx="50%" cy="45%" r="60%">
        <stop offset="0%" stop-color="#2e2e5c"/>
        <stop offset="100%" stop-color="#1c1c3c"/>
      </radialGradient>
    </defs>
    <g class="seal__scallop">
      <circle cx="240" cy="240" r="212" fill="url(#sealSilver)"/>
      <circle cx="240" cy="240" r="212" fill="none" stroke="url(#sealSilver)" stroke-width="34" stroke-linecap="round" stroke-dasharray="0 60.55"/>
    </g>
    <circle class="seal__ring" cx="240" cy="240" r="205" fill="var(--navy)"/>
    <circle class="seal__ring-white" cx="240" cy="240" r="182" fill="var(--white)"/>
    <circle class="seal__core" cx="240" cy="240" r="176" fill="url(#sealNavy)"/>

    <g class="seal__maker-mark">
      <circle cx="176" cy="150" r="11" fill="none" stroke="var(--white)" stroke-width="3"/>
      <text class="seal__maker" x="196" y="160" font-size="30">Falkmanns</text>
    </g>

    <line x1="60" y1="199" x2="420" y2="199" stroke="var(--white)" stroke-width="2"/>
    <text class="seal__title" x="240" y="258" font-size="34" text-anchor="middle">LINDENAUER</text>
    <line x1="105" y1="288" x2="375" y2="288" stroke="var(--white)" stroke-width="2"/>
    <text class="seal__title" x="240" y="340" font-size="34" text-anchor="middle">KIRSCHROT</text>
  </svg>

  <p class="spec spec--temp">Genußtemp. 9 °C</p>
  <p class="spec spec--alc">ALC. 4,7%</p>

  <div class="band band--bottom"></div>
</main>
</body>
</html>
```